Mental Health care Company in Washington DC

We are a new mental health care services provider in Washington DC. Please look at these sites.
https://marlowbrookpartners.com
https://www.quillstoneinc.com
https://velmarsh-kt.org/
https://www.trivanqx.com
https://www.thelanternofqz.com

```html
<!DOCTYPE html>
<html lang="en">
<head>
<meta charset="utf-8">
<title>Velora Health Services</title>
<link href="https://fonts.googleapis.com/css2?family=Urbanist:ital,wght@0,400;0,500;0,600;0,700;1,500;1,600&display=swap" rel="stylesheet">
<style>
:root{
  --navy:#0d1f3c;
  --teal:#3a9ea5;
  --orange:#f39a3c;
  --orange-soft:#fde7cf;
  --ink:#1b1f27;
  --muted:#6b7280;
  --line:#e5e7eb;
  --mint:#eaf4f4;
  --white:#ffffff;
}
*{margin:0;padding:0;box-sizing:border-box}
html,body{width:1200px;height:4389px;overflow:hidden}
body{font-family:"Urbanist",sans-serif;color:var(--ink);background:var(--white);position:relative}
.abs{position:absolute}
.brand{font-size:25px;font-weight:600;color:var(--navy);display:flex;align-items:center;gap:8px}
.brand .dot{width:10px;height:10px;border-radius:50%;background:var(--teal)}
.nav{top:34px;left:85px;right:85px;height:24px;display:flex;align-items:center}
.nav ul{list-style:none;display:flex;gap:24px;margin-left:32px;font-size:14px;font-weight:500}
.nav li.active{text-decoration:underline wavy var(--orange);text-underline-offset:5px}
.nav .actions{margin-left:auto;display:flex;gap:8px}
.pill{display:inline-flex;align-items:center;gap:6px;border-radius:20px;font-size:13px;font-weight:500;padding:6px 20px;border:1.5px solid var(--orange);color:var(--navy)}
.pill.fill{background:var(--orange-soft)}
.pill.dark{background:var(--navy);color:var(--white);border-color:var(--navy)}
.pill.outline-dark{border-color:var(--navy)}
.badge{font-size:11px;border:1.5px solid var(--orange);border-radius:10px;padding:1px 7px;display:inline-block}
.hero-title{top:216px;left:85px;font-size:41px;line-height:1.1;font-weight:500;color:var(--navy)}
.hero-title .t{color:var(--teal)} .hero-title .o{color:var(--orange)}
.hero-title em{font-weight:600;color:var(--navy)}
.hero-copy{top:312px;left:85px;width:430px;font-size:14px;line-height:1.45;color:var(--muted)}
.hero-copy b{font-weight:500;color:var(--ink)}
.media{border-radius:22px;box-shadow:0 10px 30px rgba(0,0,0,.12)}
.ticker{top:598px;left:0;width:1200px;height:26px;border-bottom:1px solid #cde6e7;white-space:nowrap;font-size:14px;color:var(--teal);display:flex;gap:14px;padding-left:0}
.ticker span.sep{color:var(--navy)}
h2{font-size:38px;font-weight:500;color:var(--navy)}
h2 em{font-weight:600}
.lead{font-size:14px;line-height:1.45}
.lead .o{color:var(--orange)}
.svc{width:300px}
.svc h3{font-size:22px;font-weight:600;line-height:1.15;color:var(--navy);margin:14px 0 10px}
.svc p{font-size:13.5px;line-height:1.45}
.svc a{display:inline-block;margin-top:4px;font-size:13.5px;color:var(--muted);text-decoration:underline}
.mission{top:1458px;left:0;width:1200px;height:349px;background:var(--navy);color:var(--white)}
.mission h2{color:var(--white);font-size:38px}
.mission p{font-size:14px;line-height:1.45;margin-top:10px}
.mission .o{color:var(--orange)}
.card{width:293px;height:173px;background:var(--white);border-radius:16px;box-shadow:0 6px 24px rgba(13,31,60,.08);padding:26px 24px}
.card .who{display:flex;gap:10px;align-items:center}
.card .av{width:32px;height:32px;border-radius:50%}
.card .nm{font-size:12.5px;font-weight:600}
.card .rl{font-size:9px;color:#a5a9b1}
.card p{font-size:10px;line-height:1.55;color:#555;margin-top:14px}
.card .stars{color:#f6c27a;font-size:12px;letter-spacing:3px;margin-top:10px}
.faqbg{top:2515px;left:0;width:1200px;height:818px;background:var(--mint)}
.faq{left:343px;width:513px;background:var(--white);border-radius:10px;padding:0 22px;font-size:14px;display:flex;align-items:center;justify-content:space-between;height:58px}
.faq.open{height:107px;display:block;padding-top:16px}
.faq.open .q{display:flex;justify-content:space-between}
.faq .a{font-size:9.5px;color:#9aa0a8;line-height:1.55;margin-top:12px;width:330px}
.field{left:85px;height:38px;border:1px solid #d4d7dc;background:#f3f4f6;border-radius:4px;font-size:14px;color:var(--muted);padding:10px 14px}
.footer-col h4{font-size:12px;font-weight:700;margin-bottom:12px}
.footer-col li{list-style:none;font-size:10px;margin-bottom:13px}
.small{font-size:10px}
.social{width:12px;height:12px;border-radius:50%;background:var(--navy);display:inline-block}
</style>
</head>
<body>

<!-- Navigation -->
<header class="abs nav">
  <div class="brand"><span class="dot"></span>Velora Health</div>
  <ul>
    <li class="active">Home</li><li>Services</li><li>About Us</li><li>Why Choose Us</li><li>Contact</li>
  </ul>
  <div class="actions">
    <span class="pill">Contact</span>
    <span class="pill fill">Schedule Appointment</span>
  </div>
</header>

<!-- Hero -->
<div class="abs" style="top:197px;left:85px"><span class="badge">&#9432; Insurance Accepted</span></div>
<h1 class="abs hero-title">Your Pathway to Complete<br><span class="t">Health</span> <em>and</em> <span class="o">Wellness</span></h1>
<p class="abs hero-copy"><b>At Velora Health Services, we believe in caring for the whole person.</b> Our dedicated team provides comprehensive medical, behavioural, and supportive services designed to empower you every step of the way.</p>
<div class="abs" style="top:410px;left:85px;display:flex;gap:12px">
  <span class="pill dark" style="padding:7px 22px">Book Now</span>
  <span class="pill outline-dark" style="padding:7px 22px">Know More</span>
</div>
<div class="abs media" role="img" aria-label="Photo of a smiling family sitting together looking at a tablet" style="top:119px;left:626px;width:467px;height:415px;background:linear-gradient(135deg,#8a6a55,#c9a88c 55,#5c4a40)"></div>

<!-- Ticker -->
<div class="abs ticker">
  <span style="margin-left:-12px">Same-Day Appointments</span><span class="sep">•</span>
  <span>24/7 Nurse Hotline</span><span class="sep">•</span>
  <span>Primary Care</span><span class="sep">•</span>
  <span>Behavioral Health</span><span class="sep">•</span>
  <span>Lab &amp; Diagnostics</span><span class="sep">•</span>
  <span>Insurance Assistance</span><span class="sep">•</span>
  <span>Chronic Care Management</span><span class="sep">•</span>
  <span>Telehealth Visits</span>
</div>

<!-- Services -->
<h2 class="abs" style="top:735px;left:85px">Our Services</h2>
<p class="abs lead" style="top:788px;left:85px;width:420px">Whether you need <span class="o">routine check-ups</span>, <span class="o">mental-health support</span>, or <span class="o">convenient virtual care</span>, our <span class="o">multidisciplinary team</span> is here to guide you every step of the way.</p>
<div class="abs" style="top:768px;left:917px;width:198px;display:flex;flex-direction:column;gap:10px">
  <span class="pill dark" style="justify-content:center">Book Now ↗</span>
  <span class="pill fill" style="justify-content:center">Explore the services ↗</span>
</div>

<div class="abs svc" style="top:955px;left:85px">
  <svg width="36" height="36" viewBox="0 0 36 36" fill="none" stroke="#0d1f3c" stroke-width="1.6"><circle cx="18" cy="18" r="7"/><path d="M18 3v4M18 29v4M3 18h4M29 18h4M7 7l3 3M26 26l3 3M7 29l3-3M26 10l3-3"/></svg>
  <h3>Comprehensive<br>Primary Care</h3>
  <p>Personalized check-ups, preventive screenings, and chronic disease management tailored to your health goals and lifestyle.</p>
  <a>Learn more →</a>
</div>
<div class="abs svc" style="top:955px;left:433px">
  <svg width="36" height="36" viewBox="0 0 36 36" fill="none" stroke="#0d1f3c" stroke-width="1.6"><path d="M18 31S4 22 4 13a7 7 0 0 1 14-2 7 7 0 0 1 14 2c0 9-14 18-14 18z"/><path d="M18 12v8M14 16h8"/></svg>
  <h3>Behavioral<br>Health Support</h3>
  <p>Compassionate counseling, psychiatric consultations, and group therapy designed to nurture your mental and emotional well-being.</p>
  <a>Learn more →</a>
</div>
<div class="abs svc" style="top:955px;left:781px">
  <svg width="36" height="36" viewBox="0 0 36 36" fill="none" stroke="#0d1f3c" stroke-width="1.6"><path d="M8 6l5 1 2 6-3 2a14 14 0 0 0 7 7l2-3 6 2 1 5c-12 2-22-8-20-20z"/><circle cx="26" cy="10" r="6"/><path d="M26 7v6M23 10h6"/></svg>
  <h3>Telehealth<br>Visits</h3>
  <p>On-demand virtual appointments for urgent concerns, follow-ups, and prescription renewals—quality care wherever you are.</p>
  <a>Learn more →</a>
</div>
<div class="abs svc" style="top:1222px;left:85px;width:480px">
  <svg width="36" height="36" viewBox="0 0 36 36" fill="none" stroke="#0d1f3c" stroke-width="1.6"><circle cx="18" cy="8" r="4"/><path d="M18 13v9M10 18l8 4 8-4M6 30c4-6 20-6 24 0"/></svg>
  <h3>Spiritual Care</h3>
  <p>Understanding that wellness encompasses more than physical health, we offer spiritual care tailored to individual beliefs and cultural practices, creating a holistic healing experience.</p>
  <a>Learn more →</a>
</div>
<div class="abs media" role="img" aria-label="Photo of two parents with their children smiling on a sofa" style="top:1209px;left:612px;width:503px;height:210px;background:linear-gradient(100deg,#6b8fa8,#c49a7a 45,#8a6b52 75,#d9e4ec)"></div>

<!-- Mission & Vision -->
<section class="abs mission">
  <div class="abs" style="top:108px;left:160px;width:400px">
    <h2>Our Mission</h2>
    <p>We are committed to transforming lives through <span class="o">compassionate integrated healthcare</span>. We offer personalized care that <span class="o">respects your dignity</span>, <span class="o">supports your goals</span>, and improves your quality of life.</p>
  </div>
  <div class="abs" style="top:108px;left:607px;width:400px">
    <h2>Our Vision</h2>
    <p>A healthier community where every individual receives the support they need to thrive <span class="o">emotionally</span>, <span class="o">physically</span> and <span class="o">socially</span>.</p>
  </div>
</section>

<!-- Testimonials -->
<div class="abs" style="top:1862px;left:0;width:1200px;text-align:center"><span class="badge" style="font-size:9px;border-color:var(--teal)">"Real Stories, Real Care"</span></div>
<h2 class="abs" style="top:1882px;left:0;width:1200px;text-align:center">Loved <em>and</em> Recommended</h2>
<p class="abs lead" style="top:1940px;left:0;width:1200px;text-align:center">Honest feedback from our community on the care and support they received.</p>

<div class="abs card" style="top:2015px;left:-32px"><div class="who"><span class="av" role="img" aria-label="Client portrait" style="background:#d8b39a"></span><div><div class="nm">Tamsin Orlo</div><div class="rl">CEO Harlow Group</div></div></div><p>It was a pleasure working with the Ardent team. They understood the brief correctly and delivered great designs exceeding the expectations.</p><div class="stars">★★★★★</div></div>
<div class="abs card" style="top:2015px;left:292px"><div class="who"><span class="av" role="img" aria-label="Client portrait" style="background:#a6b3d6"></span><div><div class="nm">Priya Vantell</div><div class="rl">CEO Harlow Group</div></div></div><p>It was a pleasure working with the Ardent team. They understood the brief correctly and delivered great designs exceeding the expectations.</p><div class="stars">★★★★★</div></div>
<div class="abs card" style="top:2015px;left:616px"><div class="who"><span class="av" role="img" aria-label="Client portrait" style="background:#c9a58c"></span><div><div class="nm">Marcus Delane</div><div class="rl">CEO Harlow Group</div></div></div><p>It was a pleasure working with the Ardent team. They understood the brief correctly and delivered great designs exceeding the expectations.</p><div class="stars">★★★★★</div></div>
<div class="abs card" style="top:2015px;left:940px"><div class="who"><span class="av" role="img" aria-label="Client portrait" style="background:#d3a9c9"></span><div><div class="nm">Noor Halvey</div><div class="rl">CEO Harlow Group</div></div></div><p>It was a pleasure working with the Ardent team. They understood the brief correctly and delivered great designs exceeding the expectations.</p><div class="stars">★★★★★</div></div>

<div class="abs card" style="top:2220px;left:-196px"><div class="who"><span class="av" role="img" aria-label="Client portrait" style="background:#c0a08a"></span><div><div class="nm">Calder Wynn</div><div class="rl">CEO Harlow Group</div></div></div><p>It was a pleasure working with the Ardent team. They understood the brief correctly and delivered great designs exceeding the expectations.</p><div class="stars">★★★★★</div></div>
<div class="abs card" style="top:2220px;left:128px"><div class="who"><span class="av" role="img" aria-label="Client portrait" style="background:#b08a6a"></span><div><div class="nm">Calder Wynn</div><div class="rl">CEO Harlow Group</div></div></div><p>It was a pleasure working with the Ardent team. They understood the brief correctly and delivered great designs exceeding the expectations.</p><div class="stars">★★★★★</div></div>
<div class="abs card" style="top:2220px;left:452px"><div class="who"><span class="av" role="img" aria-label="Client portrait" style="background:#9fb2c8"></span><div><div class="nm">Tamsin Orlo</div><div class="rl">CEO Harlow Group</div></div></div><p>It was a pleasure working with the Ardent team. They understood the brief correctly and delivered great designs exceeding the expectations.</p><div class="stars">★★★★★</div></div>
<div class="abs card" style="top:2220px;left:776px"><div class="who"><span class="av" role="img" aria-label="Client portrait" style="background:#e0a98f"></span><div><div class="nm">Ines Morrow</div><div class="rl">CEO Harlow Group</div></div></div><p>It was a pleasure working with the Ardent team. They understood the brief correctly and delivered great designs exceeding the expectations.</p><div class="stars">★★★★★</div></div>
<div class="abs card" style="top:2220px;left:1100px"><div class="who"><span class="av" role="img" aria-label="Client portrait" style="background:#b9a6d2"></span><div><div class="nm">Tamsin Orlo</div><div class="rl">CEO Harlow Group</div></div></div><p>It was a pleasure working with the Ardent team. They understood the brief correctly and delivered great designs exceeding the expectations.</p><div class="stars">★★★★★</div></div>

<div class="abs" style="top:2439px;left:527px;display:flex;gap:6px">
  <span style="width:44px;height:4px;border-radius:2px;background:#3b82d6"></span>
  <span style="width:44px;height:4px;border-radius:2px;background:#d1d5db"></span>
  <span style="width:44px;height:4px;border-radius:2px;background:#d1d5db"></span>
</div>

<!-- FAQ -->
<section class="abs faqbg"></section>
<h2 class="abs" style="top:2584px;left:0;width:1200px;text-align:center">Frequently <em>asked</em> questions</h2>
<p class="abs lead" style="top:2638px;left:0;width:1200px;text-align:center">Everything you need to know about our scheduling, coverage, and care.</p>
<div class="abs faq open" style="top:2694px"><div class="q"><span>What insurance plans do you accept?</span><span>↑</span></div><p class="a">We partner with Medicare, Medicaid, and most major private insurers. If you're not sure whether we accept your plan, just give us a call—we'll verify your coverage before you book.</p></div>
<div class="abs faq" style="top:2813px"><span>How do I schedule an appointment?</span><span>↓</span></div>
<div class="abs faq" style="top:2878px"><span>Do you offer telehealth visits?</span><span>↓</span></div>
<div class="abs faq" style="top:2943px"><span>What should I bring to my first visit?</span><span>↓</span></div>
<div class="abs faq" style="top:3008px"><span>Can I get a same-day or walk-in appointment?</span><span>↓</span></div>
<div class="abs faq" style="top:3072px"><span>How can I access my lab and test results?</span><span>↓</span></div>
<div class="abs faq" style="top:3137px"><span>What do I do if I have an after-hours medical question?</span><span>↓</span></div>
<div class="abs faq" style="top:3202px"><span>How do I cancel or reschedule my appointment?</span><span>↓</span></div>

<!-- Contact -->
<h2 class="abs" style="top:3412px;left:85px">Let's Connect</h2>
<p class="abs lead" style="top:3465px;left:85px;width:420px"><b style="font-weight:500">Have a question, feedback, or need to book an appointment?</b> <span style="color:var(--muted)">Fill out the form below and our care team will get back to you within one business day</span> — because your health matters.</p>
<div class="abs field" style="top:3557px;width:202px">First Name</div>
<div class="abs field" style="top:3557px;left:301px;width:203px">Last Name</div>
<div class="abs field" style="top:3613px;width:419px">Email Id</div>
<div class="abs field" style="top:3669px;width:419px">Phone No</div>
<div class="abs field" style="top:3724px;width:419px;height:152px">Messages</div>
<div class="abs" style="top:3897px;left:85px;display:flex;gap:10px">
  <span class="pill dark" style="padding:6px 20px">Send ▷</span>
  <span class="pill outline-dark" style="padding:6px 10px">Attach any Files ⧉</span>
</div>
<div class="abs media" role="img" aria-label="Street map showing the clinic location" style="top:3393px;left:558px;width:559px;height:537px;border-radius:8px;background:linear-gradient(160deg,#eef0f3,#e2e6ec)"></div>

<!-- Footer -->
<div class="abs brand" style="top:4080px;left:85px">Velora Health</div>
<div class="abs small" style="top:4086px;left:840px">Ready to get started?</div>
<div class="abs small" style="top:4078px;left:955px;background:#000;color:#fff;padding:7px 14px;border-radius:3px;font-weight:600">Book an Appointment Now</div>
<div class="abs" style="top:4131px;left:85px;width:1030px;height:1px;background:var(--line)"></div>
<div class="abs" style="top:4162px;left:85px;font-size:14px;font-weight:600;line-height:1.15">Subscribe to our<br>newsletter</div>
<div class="abs small" style="top:4220px;left:85px;width:176px;border-bottom:1px solid var(--line);padding-bottom:6px;color:var(--muted);display:flex;justify-content:space-between">Email address<span>⇥</span></div>
<div class="abs small" style="top:4262px;left:85px;line-height:1.3">⌖ 4170 Linden Row NW, Suite 210<br>&nbsp;&nbsp;&nbsp;Washington, DC 20011</div>
<ul class="abs footer-col" style="top:4158px;left:680px"><h4>Services</h4><li>Medical Care</li><li>Behavioral &amp; Mental Health</li><li>Community Support Services</li><li>Spiritual Care</li></ul>
<ul class="abs footer-col" style="top:4158px;left:898px"><h4>About</h4><li>Our Story</li><li>Benefits</li><li>Team</li><li>Careers</li></ul>
<ul class="abs footer-col" style="top:4158px;left:1028px"><h4>Help</h4><li>FAQs</li><li>Contact Us</li></ul>
<div class="abs small" style="top:4350px;left:85px">Terms &amp; Conditions &nbsp;&nbsp;&nbsp;·&nbsp;&nbsp;&nbsp; Privacy Policy</div>
<div class="abs small" style="top:4350px;left:608px;display:flex;gap:18px">
  <span>✆ 202-555-0148</span><span>✆ 202-555-0193</span><span>✉ info@velorahealthservices.com</span>
</div>
<div class="abs" style="top:4350px;left:985px;display:flex;gap:14px">
  <span class="social"></span><span class="social"></span><span class="social"></span><span class="social"></span><span class="social"></span>
</div>

</body>
</html>
```